Frostwyn.co - Polar Expeditions Specialists

We need a modern, visually striking business card for Frostwyn.co, a company specialized in selling expedition cruises to the most remote regions on Earth, with a focus on the Arctic and Antarctica. The design should instantly communicate that the cardholder is an expert in polar travel. Use clean, premium aesthetics with cool tones like icy blue and white, possibly incorporating polar imagery (ice, glaciers, penguins, etc.)

Attached the logo

Contact Information for Business Card

Feels high-end and trustworthy.. Visually memorable — encourages people to keep it

Colors
0054AA
0677BA
7BADD7
CADEEF
E8F1F8

Requirements
Must have
• ice, glaciers, penguins, montains
Nice to have
• modern, transparente,

```html
<!DOCTYPE html>
<html lang="en">
<head>
<meta charset="utf-8">
<title>Frostwyn.co Business Card</title>
<link href="https://fonts.googleapis.com/css2?family=Poppins:wght@400;500;600;700&display=swap" rel="stylesheet">
<style>
  :root {
    --page-bg: #d3d4d6;
    --brand-blue: #2f6cb3;
    --photo-top: #6683b6;
    --photo-mid: #5a7ab2;
    --photo-low: #7391c2;
    --white: #ffffff;
  }
  * { margin: 0; padding: 0; box-sizing: border-box; }
  html, body { width: 900px; height: 1200px; overflow: hidden; }
  body {
    background: var(--page-bg);
    font-family: "Poppins", sans-serif;
    position: relative;
  }
  .card {
    position: absolute;
    left: 134px;
    width: 632px;
    height: 364px;
    overflow: hidden;
  }
  .card-front { top: 212px; }
  .card-back { top: 624px; background: var(--white); }

  .front-photo {
    position: absolute; inset: 0;
    background: linear-gradient(180deg, var(--photo-top) 0%, var(--photo-mid) 55%, var(--photo-low) 100%);
  }
  .front-mark {
    position: absolute; left: 50%; top: 66px;
    width: 96px; height: 96px; margin-left: -48px;
    border-radius: 50%; background: var(--white);
  }
  .front-wordmark {
    position: absolute; left: 0; right: 0; top: 208px;
    text-align: center; color: var(--white);
    font-weight: 700; font-size: 60px; line-height: 1; letter-spacing: -0.3px;
  }
  .front-tagline {
    position: absolute; left: 0; right: 0; top: 286px;
    text-align: center; color: var(--white);
    font-weight: 600; font-size: 21px; line-height: 1;
  }

  .back-brand {
    position: absolute; left: 36px; width: 300px; top: 100px;
    text-align: center; color: var(--brand-blue);
  }
  .back-mark {
    width: 78px; height: 78px; margin: 0 auto;
    border-radius: 50%; background: var(--brand-blue);
  }
  .back-wordmark {
    margin-top: 24px; font-weight: 700; font-size: 37px; line-height: 1; letter-spacing: -0.2px;
  }
  .back-tagline {
    margin-top: 10px; font-weight: 600; font-size: 14px; line-height: 1;
  }
  .divider {
    position: absolute; left: 347px; top: 92px;
    width: 2px; height: 180px; background: var(--brand-blue);
  }
  .contact {
    position: absolute; left: 378px; top: 104px; color: var(--brand-blue);
  }
  .contact-name {
    font-weight: 700; font-size: 21px; line-height: 1; letter-spacing: 0.8px; text-transform: uppercase;
  }
  .contact-role {
    font-weight: 500; font-size: 14px; line-height: 1; letter-spacing: 1.5px; margin-top: 4px;
  }
  .contact-list { list-style: none; margin-top: 9px; }
  .contact-list li {
    display: flex; align-items: center; gap: 6px;
    font-size: 15.5px; line-height: 22px; letter-spacing: 1px;
  }
  .contact-list svg { width: 13px; height: 13px; flex: none; fill: var(--brand-blue); }
</style>
</head>
<body>
  <section class="card card-front">
    <div class="front-photo" role="img" aria-label="Blue-tinted photo of a penguin on snowy ice with a glacier and mountains behind"></div>
    <div class="front-mark"></div>
    <div class="front-wordmark">Frostwyn.co</div>
    <div class="front-tagline">Polar Expeditions Specialists</div>
  </section>

  <section class="card card-back">
    <div class="back-brand">
      <div class="back-mark"></div>
      <div class="back-wordmark">Frostwyn.co</div>
      <div class="back-tagline">Polar Expeditions Specialists</div>
    </div>
    <div class="divider"></div>
    <div class="contact">
      <div class="contact-name">Mara Lindqvist</div>
      <div class="contact-role">CEO</div>
      <ul class="contact-list">
        <li><svg viewBox="0 0 24 24" aria-hidden="true"><path d="M6.6 10.8a15 15 0 0 0 6.6 6.6l2.2-2.2a1 1 0 0 1 1-.25 11.4 11.4 0 0 0 3.6.57 1 1 0 0 1 1 1V20a1 1 0 0 1-1 1A17 17 0 0 1 3 4a1 1 0 0 1 1-1h3.5a1 1 0 0 1 1 1c0 1.25.2 2.45.57 3.57a1 1 0 0 1-.25 1z"/></svg>(555) 201-4478</li>
        <li><svg viewBox="0 0 24 24" aria-hidden="true"><path d="M2 5h20v2l-10 6L2 7zM2 9l10 6 10-6v10H2z"/></svg>info@Frostwyn.co</li>
        <li><svg viewBox="0 0 24 24" aria-hidden="true"><path d="M12 2a10 10 0 1 0 0 20 10 10 0 0 0 0-20zm0 2c1 1.3 1.8 3.6 2 6h-4c.2-2.4 1-4.7 2-6zM4.1 10a8 8 0 0 1 4-5.3A14 14 0 0 0 8 10zm0 4H8c.1 1.9.5 3.7 1.1 5.3A8 8 0 0 1 4.1 14zM12 20c-1-1.3-1.8-3.6-2-6h4c-.2 2.4-1 4.7-2 6zm2.9-.7c.6-1.6 1-3.4 1.1-5.3h3.9a8 8 0 0 1-5 5.3zM16 10a14 14 0 0 0-1.1-5.3A8 8 0 0 1 19.9 10z"/></svg>www.Frostwyn.co</li>
        <li><svg viewBox="0 0 24 24" aria-hidden="true"><circle cx="12" cy="12" r="10"/></svg>/frostwyn</li>
        <li><svg viewBox="0 0 24 24" aria-hidden="true"><circle cx="12" cy="12" r="10"/></svg>/frostwyn</li>
      </ul>
    </div>
  </section>
</body>
</html>
```